Web Design Project

We are an IT System Integrator. We provide Norvik 500 ERP System, CRM etc. We also provide hardware, networking servicing. Please look at www.brinquot.com.sg. They provide the same service as us. We like to redesign our web site. I will attached the color that I prefer for reference.

Our website is www.ravdu.com.sg.  It has been created about 14 years ago.  We are trying to revamp it with a new look and information.   The new website must be informative, fast.    I have attached an attachment which show the color that I prefer(brownish golden).   

Our competitor (www.brinquot.com) is carrying the same trade as us.  They have all the informations In their website that we will like to have.  Therefore I recommend you to take a look at my competitor website and have a better   
understanding on the kind of information I would like to have for my new website.

This project is guarantee to the person with the best design.  We can have it guarantee.

Target Market(s)

Corporate and companies

Industry/Entity Type

Hardware

```html
<!DOCTYPE html>
<html lang="en">
<head>
<meta charset="utf-8">
<title>Ravdu Information Systems PTE LTD</title>
<link href="https://fonts.googleapis.com/css2?family=Exo+2:wght@300;400;500&family=Arimo:ital,wght@0,400;0,700;1,400;1,700&display=swap" rel="stylesheet">
<style>
:root{
  --gold:#f5b731;
  --gold-deep:#d9a23a;
  --dot:#e8d9a4;
  --charcoal:#2f2f2f;
  --bar:#333333;
  --ink:#2a2a2a;
  --grey-text:#9a9a9a;
  --white:#ffffff;
}
*{box-sizing:border-box;margin:0;padding:0}
html,body{width:1200px;height:1054px;overflow:hidden;background:var(--white)}
.canvas{position:relative;width:1200px;height:1054px;overflow:hidden;font-family:"Arimo",Arial,sans-serif;color:var(--ink)}

.top-bar{position:absolute;left:0;top:0;width:1200px;height:46px;background:var(--bar)}
.utility-links{position:absolute;left:746px;top:18px;font-size:10.5px;color:var(--white);letter-spacing:.2px}
.utility-links span{margin:0 5px}
.utility-icons{position:absolute;left:940px;top:12px;display:flex;gap:12px;align-items:center}
.utility-icons i{display:block;width:20px;height:20px;border-radius:50%;background:var(--gold)}

.hero{position:absolute;left:0;top:46px;width:1200px;height:600px}
.hero-photo{position:absolute;inset:0;background:
  linear-gradient(180deg,rgba(245,245,243,.85) 0%,rgba(245,245,243,.2) 40%,rgba(245,245,243,0) 100%),
  linear-gradient(90deg,#b7cadd 0%,#d9dde2 22%,#e6e3df 45%,#d8d2cc 62%,#e2d3c3 80%,#8a909b 100%)}
.hero-curve{position:absolute;left:0;top:0}

.hero-title{position:absolute;left:0;width:1200px;top:392px;text-align:center;font-family:"Exo 2",sans-serif;font-weight:300;font-size:54px;letter-spacing:-1px;color:var(--charcoal);line-height:1}
.hero-sub{position:absolute;left:0;width:1200px;top:454px;text-align:center;font-family:"Exo 2",sans-serif;font-size:15px;color:#111;line-height:1}
.hero-dots{position:absolute;left:536px;top:485px;display:flex;gap:18px}
.hero-dots i{display:block;width:12px;height:12px;border-radius:50%;background:var(--dot)}
.hero-dots i.is-active{background:var(--gold-deep);box-shadow:0 0 0 2px #fff inset}
.slider-arrow{position:absolute;top:538px;width:52px;height:52px;border-radius:50%;background:var(--white);display:flex;align-items:center;justify-content:center}
.slider-arrow.prev{left:42px}
.slider-arrow.next{left:1122px}

.header-logo{position:absolute;left:180px;top:70px;display:flex;align-items:center;gap:12px}
.logo-mark{width:40px;height:40px;border-radius:50%;background:var(--gold)}
.logo-name{font-family:"Exo 2",sans-serif;font-weight:400;font-size:25px;line-height:1.05;color:#3b3b3b}

.main-nav{position:absolute;left:0;top:46px;width:1200px;height:97px;font-family:"Exo 2",sans-serif;font-size:15px;color:#222}
.main-nav a{position:absolute;top:0;height:97px;padding-top:47px;color:inherit;text-decoration:none;white-space:nowrap;letter-spacing:-.2px}
.main-nav a.is-active{left:467px;width:58px;background:#222;color:var(--white);border-top:8px solid var(--gold);padding-top:39px;text-align:center}

.service-tiles{position:absolute;left:263px;top:520px;display:flex;gap:49px}
.tile{position:relative;width:137px;height:157px}
.tile svg{position:absolute;inset:0}
.tile-label{position:absolute;left:0;width:137px;top:100px;text-align:center;font-family:"Exo 2",sans-serif;font-size:15px;line-height:20px;color:var(--gold)}

.about{position:absolute;left:185px;top:714px;width:560px}
.about h1{font-family:"Exo 2",sans-serif;font-weight:400;font-size:23px;color:#222;letter-spacing:-.3px}
.about h1 em{font-style:normal;color:var(--gold-deep)}
.about p{margin-top:9px;font-size:12.5px;line-height:17.4px;color:var(--grey-text)}

.testimonials{position:absolute;left:768px;top:713px;width:260px}
.testimonials h2{font-family:"Exo 2",sans-serif;font-weight:400;font-size:21px;letter-spacing:1px;color:#222}
.quote{position:relative;margin-top:13px;padding-left:25px;padding-right:20px;font-size:10.5px;line-height:15px;color:#555}
.quote-mark{position:absolute;font-family:Georgia,serif;font-size:30px;font-weight:700;color:#555;line-height:1}
.quote-mark.open{left:0;top:-6px}
.quote-mark.close{right:0;top:22px}
.quote-author{margin-top:10px;margin-left:148px;font-size:10px;font-weight:700;font-style:italic;color:#444}
.quote-role{margin-left:148px;font-size:10px;font-style:italic;color:#444}

.partners{position:absolute;left:180px;top:875px;width:848px;height:59px;background:linear-gradient(180deg,#fafafa,#ececec);box-shadow:0 2px 3px rgba(0,0,0,.12);display:flex;align-items:center}
.partners h2{width:236px;padding-left:27px;font-family:"Exo 2",sans-serif;font-weight:400;font-size:21px;letter-spacing:1px;color:#222;border-right:1px solid #ddd;height:45px;line-height:45px}
.partner{height:45px;display:flex;align-items:center;justify-content:center;border-right:1px solid #ddd;font-family:"Exo 2",sans-serif;font-weight:500}
.partner:last-child{border-right:none}
.partner-badge{width:48px;height:48px;border-radius:50%;border:2px solid #2a3a9a;background:#fff}
.partner.green{color:#0e6b3a}
.partner.blue{color:#1d3a8c}

.footer{position:absolute;left:0;top:947px;width:1200px;height:107px;background:var(--bar)}
.footer-nav{position:absolute;left:180px;top:31px;font-size:12px;color:var(--white)}
.footer-nav span{color:var(--gold);margin:0 8px;font-style:italic}
.copyright{position:absolute;left:180px;top:62px;font-size:10.5px;color:#ddd}
.footer-social{position:absolute;left:641px;top:27px;display:flex;gap:8px}
.footer-social i{display:block;width:21px;height:21px;border-radius:50%;background:var(--white)}
.footer-logo{position:absolute;left:780px;top:24px;display:flex;align-items:center;gap:10px}
.footer-logo .logo-name{font-size:17px;color:var(--white)}
.footer-logo .logo-mark{width:30px;height:30px}
</style>
</head>
<body>
<div class="canvas">

  <div class="top-bar">
    <div class="utility-links">FAQs<span>|</span>Resources<span>|</span>Contact Us</div>
    <div class="utility-icons">
      <svg width="27" height="18" viewBox="0 0 27 18" aria-label="Email"><rect x="0" y="0" width="27" height="18" fill="#f5b731"/><path d="M1 1 L13.5 10 L26 1" fill="none" stroke="#333" stroke-width="2"/></svg>
      <i aria-label="Social link"></i>
      <i aria-label="Social link"></i>
    </div>
  </div>

  <section class="hero">
    <div class="hero-photo" role="img" aria-label="Photo of a smiling business team seated together in a bright office"></div>
    <svg class="hero-curve" width="1200" height="600" viewBox="0 0 1200 600" aria-hidden="true">
      <path d="M0 588 C300 552 520 544 640 545 C820 547 1020 562 1200 586 L1200 600 L0 600 Z" fill="#ffffff"/>
    </svg>
  </section>

  <div class="hero-title">CUSTOMER RELATIONSHIP</div>
  <div class="hero-sub">Shorten sales cycle and achieve total customer satisfaction.</div>
  <div class="hero-dots"><i class="is-active"></i><i></i><i></i><i></i><i></i><i></i></div>

  <div class="slider-arrow prev"><svg width="22" height="22" viewBox="0 0 22 22"><path d="M15 2 L5 11 L15 20" fill="none" stroke="#111" stroke-width="5"/></svg></div>
  <div class="slider-arrow next"><svg width="22" height="22" viewBox="0 0 22 22"><path d="M7 2 L17 11 L7 20" fill="none" stroke="#111" stroke-width="5"/></svg></div>

  <div class="header-logo">
    <div class="logo-mark"></div>
    <div class="logo-name">Ravdu Information<br>Systems PTE LTD</div>
  </div>

  <nav class="main-nav">
    <a class="is-active">HOME</a>
    <a style="left:539px">ABOUT US</a>
    <a style="left:629px">SOLUTIONS</a>
    <a style="left:728px">SERVICES</a>
    <a style="left:816px">EVENT &amp; PROMOTION</a>
    <a style="left:971px">OUR CLIENTS</a>
  </nav>

  <div class="service-tiles">
    <div class="tile">
      <svg width="137" height="157" viewBox="0 0 137 157">
        <defs><linearGradient id="hexFill" x1="0" y1="0" x2="0" y2="1"><stop offset="0" stop-color="#3a3a3a"/><stop offset="1" stop-color="#1f1f1f"/></linearGradient></defs>
        <polygon points="68.5,0 137,39 137,118 68.5,157 0,118 0,39" fill="url(#hexFill)"/>
        <rect x="36" y="33" width="14" height="50" rx="2" fill="#f5b731"/>
        <rect x="54" y="33" width="46" height="34" rx="3" fill="#f5b731"/>
        <rect x="58" y="37" width="38" height="26" fill="#2c2c2c"/>
        <rect x="73" y="67" width="8" height="9" fill="#f5b731"/>
        <rect x="62" y="76" width="30" height="5" fill="#f5b731"/>
      </svg>
      <div class="tile-label">WORKSTATIONS</div>
    </div>
    <div class="tile">
      <svg width="137" height="157" viewBox="0 0 137 157">
        <polygon points="68.5,0 137,39 137,118 68.5,157 0,118 0,39" fill="url(#hexFill)"/>
        <rect x="49" y="26" width="39" height="65" rx="2" fill="#f5b731"/>
        <g stroke="#2c2c2c" stroke-width="2"><line x1="53" y1="34" x2="84" y2="34"/><line x1="53" y1="40" x2="84" y2="40"/><line x1="53" y1="46" x2="84" y2="46"/><line x1="53" y1="52" x2="84" y2="52"/></g>
        <circle cx="68.5" cy="79" r="3" fill="#2c2c2c"/>
      </svg>
      <div class="tile-label">SERVERS</div>
    </div>
    <div class="tile">
      <svg width="137" height="157" viewBox="0 0 137 157">
        <polygon points="68.5,0 137,39 137,118 68.5,157 0,118 0,39" fill="url(#hexFill)"/>
        <rect x="49" y="30" width="39" height="15" rx="2" fill="#f5b731"/>
        <rect x="37" y="47" width="63" height="26" rx="6" fill="#f5b731"/>
        <rect x="49" y="61" width="39" height="28" rx="2" fill="#f5b731" stroke="#2c2c2c" stroke-width="3"/>
        <g stroke="#2c2c2c" stroke-width="2.5"><line x1="55" y1="70" x2="82" y2="70"/><line x1="55" y1="77" x2="82" y2="77"/></g>
      </svg>
      <div class="tile-label">PRINTERS</div>
    </div>
    <div class="tile">
      <svg width="137" height="157" viewBox="0 0 137 157">
        <polygon points="68.5,0 137,39 137,118 68.5,157 0,118 0,39" fill="url(#hexFill)"/>
        <rect x="58" y="25" width="21" height="8" rx="3" fill="#f5b731"/>
        <circle cx="68.5" cy="59" r="26" fill="#f5b731"/>
        <circle cx="68.5" cy="59" r="18" fill="#2c2c2c"/>
        <circle cx="68.5" cy="59" r="11" fill="#f5b731"/>
        <circle cx="63" cy="54" r="4" fill="#2c2c2c"/>
      </svg>
      <div class="tile-label">SURVEILLANCE<br>CAMERA</div>
    </div>
  </div>

  <section class="about">
    <h1>RAVDU INFORMATION SYSTEMS <em>PTE LTD (RIS)</em></h1>
    <p>is professionally managed by a core group of visionaries and technologists with decades of industry experience between them and backed by a team of trained professionals at all levels of operations. Perfection is a way of life at RIS. The organization has grown from a small beginning in 1993, to become a company of international repute for reliability. RIS has transformed from a Norvik Reseller to a company providing total IT solutions to companies in Singapore and the Asia region. RIS provides hardware maintenance, networking, software and consulting services.</p>
  </section>

  <aside class="testimonials">
    <h2>TESTIMONIALS</h2>
    <div class="quote">
      <span class="quote-mark open">&ldquo;</span>
      We would like to express our appreciation for the prompt and efficient service provided by
      <span class="quote-mark close">&rdquo;</span>
    </div>
    <div class="quote-author">Colin Marsh</div>
    <div class="quote-role">Chief Professor</div>
  </aside>

  <section class="partners">
    <h2>MEDIA PARTNERS</h2>
    <div class="partner" style="width:190px;justify-content:flex-end;padding-right:22px"><div class="partner-badge"></div></div>
    <div class="partner green" style="width:112px;font-size:26px">Norvik</div>
    <div class="partner green" style="width:162px;font-size:18px">Norvik Ledger ERP</div>
    <div class="partner blue" style="width:146px;font-size:22px">Keltra</div>
  </section>

  <footer class="footer">
    <div class="footer-nav">Home<span>/</span>About Us<span>/</span>Solutions<span>/</span>Services<span>/</span>Event &amp; Promotion<span>/</span>Our Clients</div>
    <div class="copyright">Copyrights © 2013 Ravdu Information Systems PTE LTD. All rights reserved.</div>
    <div class="footer-social"><i aria-label="Social link"></i><i aria-label="Social link"></i><i aria-label="Social link"></i><i aria-label="Social link"></i></div>
    <div class="footer-logo">
      <div class="logo-name">Ravdu Information<br>Systems PTE LTD</div>
      <div class="logo-mark"></div>
    </div>
  </footer>

</div>
</body>
</html>
```